Moltven Advisory e-Flyer Design

Need 6 or so one pagers done. To be used to email to clients. Each to look similar with slight variations. Attached is an example done for a completely different organization, but it has the style we are looking for, and it is energetic and corporate.

```html
<!DOCTYPE html>
<html lang="en">
<head>
<meta charset="utf-8">
<title>Moltven Advisory e-Flyer</title>
<link rel="stylesheet" href="https://fonts.googleapis.com/css2?family=Archivo+Black&family=Arimo:wght@400;700&display=swap">
<style>
  :root {
    --brand-red: #d3121f;
    --panel-dark: #231f20;
    --paper: #ffffff;
    --ink: #1a1a1a;
    --sky-top: #2b3a55;
    --sky-mid: #55617a;
    --city-glow: #c9782f;
    --city-dark: #16151a;
  }
  * { box-sizing: border-box; margin: 0; padding: 0; }
  html, body {
    width: 1120px; height: 1200px; overflow: hidden;
    background: var(--paper);
  }
  .flyer {
    position: relative; width: 1120px; height: 1200px;
    font-family: "Arimo", Arial, sans-serif;
  }
  .hero {
    position: absolute; left: 0; top: 0; width: 1120px; height: 680px;
    background:
      radial-gradient(ellipse 60% 35% at 55% 75%, rgba(214,134,52,0.75), transparent 70%),
      radial-gradient(ellipse 30% 25% at 85% 60%, rgba(90,110,200,0.35), transparent 70%),
      linear-gradient(180deg, var(--sky-top) 0%, var(--sky-mid) 18%, #3a3f52 32%, #2a2a33 55%, var(--city-glow) 85%, var(--city-dark) 100%);
  }
  .hero-tower {
    position: absolute; left: 0; top: 0; width: 290px; height: 680px;
    background: linear-gradient(180deg, #101218, #1c1a1f 60%, #2a2218);
    opacity: 0.85;
  }
  .brand-tile {
    position: absolute; left: 60px; top: 0; width: 174px; height: 214px;
    background: var(--paper);
    display: flex; flex-direction: column; align-items: center; justify-content: center;
    color: var(--brand-red); font-weight: 700; text-align: center;
  }
  .brand-tile .brand-name { font-size: 30px; line-height: 1.1; letter-spacing: 0.5px; }
  .info-panel {
    position: absolute; left: 0; top: 680px; width: 1120px; height: 428px;
    background: var(--panel-dark); color: var(--paper);
    padding: 68px 60px 0 60px;
  }
  .info-block + .info-block { margin-top: 26px; }
  .info-heading {
    font-family: "Archivo Black", Arial, sans-serif;
    font-size: 23px; line-height: 1.1; margin-bottom: 4px; letter-spacing: 0.2px;
  }
  .info-text {
    font-size: 19.5px; line-height: 25.6px; text-align: justify;
  }
  .contact-bar {
    position: absolute; left: 0; top: 1108px; width: 1120px; height: 92px;
    background: var(--paper); color: var(--ink);
    display: flex; align-items: center; justify-content: space-between;
    padding: 0 40px 0 48px;
    font-size: 23px;
  }
  .contact-item { display: flex; align-items: center; gap: 8px; white-space: nowrap; }
  .contact-item svg { flex: none; }
</style>
</head>
<body>
<div class="flyer">
  <div class="hero" role="img" aria-label="Night-time city skyline with lit towers, a river, a highway with light trails and a construction crane">
    <div class="hero-tower"></div>
  </div>

  <div class="brand-tile">
    <span class="brand-name">Moltven</span>
    <span class="brand-name">Advisory</span>
  </div>

  <section class="info-panel">
    <div class="info-block">
      <h2 class="info-heading">Who We Are</h2>
      <p class="info-text">At Moltven Advisory, we specialize in strategy clarification and aligned execution. We are executives with global operations and front-line experience who help drive your business performance. Our proven Keystone method works across industries, geographies, as well as organization types and sizes.</p>
    </div>
    <div class="info-block">
      <h2 class="info-heading">Why Choose Moltven</h2>
      <p class="info-text">Moltven brings you and each member of your team a framework of strategy clarification and aligned execution - the only true competitive differentiator for organizations today. Without that framework on matters big and small, organizations, at best, misuse time and resources and don't maximize performance potential, or, at worst case, lose market share or more. Nothing is left to chance with Moltven.</p>
    </div>
  </section>

  <footer class="contact-bar">
    <div class="contact-item">
      <svg width="22" height="30" viewBox="0 0 22 30" aria-hidden="true">
        <path d="M5 2 L9 7 L6 10 C7 15 10 20 14 23 L17 20 L21 25 L17 29 C9 26 2 16 1 6 Z" fill="var(--brand-red)"/>
      </svg>
      <span>+1 212 555 0147</span>
    </div>
    <div class="contact-item">
      <svg width="34" height="24" viewBox="0 0 34 24" aria-hidden="true">
        <rect x="1" y="2" width="32" height="20" fill="var(--brand-red)"/>
        <path d="M1 2 L17 14 L33 2 M1 22 L13 11 M33 22 L21 11" stroke="#fff" stroke-width="2" fill="none"/>
      </svg>
      <span>hello@moltvenadvisory.com</span>
    </div>
    <div class="contact-item">
      <svg width="24" height="34" viewBox="0 0 24 34" aria-hidden="true">
        <path d="M12 1 C5 1 1 6 1 12 C1 20 12 33 12 33 C12 33 23 20 23 12 C23 6 19 1 12 1 Z" fill="var(--brand-red)"/>
        <circle cx="12" cy="12" r="4.5" fill="#fff"/>
      </svg>
      <span>52 W 71st St #3, New York, NY 10023</span>
    </div>
  </footer>
</div>
</body>
</html>
```